Deactivated Coal-Fired Power Plant to be redeveloped into a Green Energy Campus.

Want a striking business card statement that introduces our concept project to provide economic and community recovery to a former rural coal community in western PA.
Essentially 12 project representatives that will lead both the demolition of an existing power plant and the redevelopment to a new Green energy site.
Business Card should reflect our effort.
We are open to ideas.

Target Market(s)

Energy and Power Generation industries

Industry/Entity Type

Power Generation and Data Centers

Contact Information for Business Card

Included in uploaded materials

Font styles to use
Sans Serif
Other font styles liked:
• Arial, Calibri

Requirements
Must have
• Multiple colors

```html
<!DOCTYPE html>
<html lang="en">
<head>
<meta charset="utf-8">
<title>Ridgefield Renewal – Business Card</title>
<link href="https://fonts.googleapis.com/css2?family=Outfit:wght@400;500;700&display=swap" rel="stylesheet">
<style>
  :root {
    --bg: #2a2e33;
    --card: #f1f1f1;
    --ink: #141414;
    --green: #1f9a43;
    --green-dark: #147a32;
    --grey-photo: #d4d6d8;
    --sky: #b9cdd8;
    --field: #7fa55a;
  }
  * { box-sizing: border-box; margin: 0; padding: 0; }
  html, body { width: 1200px; height: 780px; overflow: hidden; }
  body {
    background: var(--bg);
    font-family: "Outfit", Arial, sans-serif;
    display: flex;
    align-items: center;
    justify-content: center;
    gap: 56px;
  }
  .card {
    position: relative;
    width: 520px;
    height: 298px;
    border-radius: 18px;
    background: var(--card);
    overflow: hidden;
    box-shadow: 0 14px 30px rgba(0,0,0,.45);
  }

  /* brand block (shared) */
  .brand { display: flex; align-items: center; gap: 12px; }
  .brand-dot { border-radius: 50%; background: var(--green); flex: none; }
  .brand-name {
    font-weight: 700;
    color: var(--ink);
    text-transform: uppercase;
    line-height: 1.02;
    letter-spacing: .5px;
  }

  /* back: contact side */
  .card-back .brand { position: absolute; left: 210px; top: 46px; }
  .card-back .brand-dot { width: 62px; height: 62px; }
  .card-back .brand-name { font-size: 24px; }
  .rule {
    position: absolute; left: 36px; right: 36px; top: 150px;
    height: 2px; background: var(--green);
  }
  .person { position: absolute; left: 36px; top: 170px; }
  .person-name { font-size: 22px; font-weight: 700; color: var(--ink); }
  .person-role, .person-company { font-size: 14px; color: var(--green); margin-top: 3px; }
  .contacts {
    position: absolute; right: 36px; bottom: 34px;
    list-style: none; display: flex; flex-direction: column; gap: 7px;
  }
  .contact { display: flex; align-items: center; gap: 9px; font-size: 15px; color: var(--ink); }
  .contact-icon {
    width: 20px; height: 20px; border-radius: 50%;
    background: var(--green); display: grid; place-items: center; flex: none;
  }
  .contact-icon svg { width: 11px; height: 11px; }

  /* front: brand side */
  .card-front .scene {
    position: absolute; inset: 0;
    background:
      radial-gradient(circle at 50% 48%, rgba(255,255,255,.85) 0 22%, rgba(255,255,255,0) 45%),
      linear-gradient(100deg, var(--grey-photo) 0%, #e6e7e8 38%, var(--sky) 70%, var(--field) 100%);
  }
  .card-front .brand {
    position: absolute; left: 50%; top: 50%;
    transform: translate(-50%, -50%);
  }
  .card-front .brand-dot { width: 84px; height: 84px; }
  .card-front .brand-name { font-size: 34px; }
</style>
</head>
<body>

  <article class="card card-back">
    <div class="brand">
      <span class="brand-dot"></span>
      <span class="brand-name">Ridgefield<br>Renewal</span>
    </div>
    <div class="rule"></div>
    <div class="person">
      <p class="person-name">Daniel Marsh</p>
      <p class="person-role">Chief Operating Officer</p>
      <p class="person-company">Ridgefield Renewal LLC.</p>
    </div>
    <ul class="contacts">
      <li class="contact">
        <span class="contact-icon"><svg viewBox="0 0 12 12"><rect x="1" y="2.5" width="10" height="7" rx="1" fill="none" stroke="#fff" stroke-width="1.2"/><path d="M1.5 3l4.5 3.5L10.5 3" fill="none" stroke="#fff" stroke-width="1.2"/></svg></span>
        dmarsh@ridgefieldrenewal.com
      </li>
      <li class="contact">
        <span class="contact-icon"><svg viewBox="0 0 12 12"><path d="M3 1.5l1.8 2.3-1 1.2a7 7 0 0 0 3.2 3.2l1.2-1 2.3 1.8-1 1.5C5.5 10.5 1.5 6.5 1.5 2.5z" fill="#fff"/></svg></span>
        120-340-560
      </li>
      <li class="contact">
        <span class="contact-icon"><svg viewBox="0 0 12 12"><rect x="3.5" y="1" width="5" height="10" rx="1" fill="none" stroke="#fff" stroke-width="1.2"/><circle cx="6" cy="9" r=".7" fill="#fff"/></svg></span>
        780-910-230
      </li>
    </ul>
  </article>

  <article class="card card-front">
    <div class="scene" role="img" aria-label="Photo blend of a former coal power plant fading into wind turbines, solar panels and green fields"></div>
    <div class="brand">
      <span class="brand-dot"></span>
      <span class="brand-name">Ridgefield<br>Renewal</span>
    </div>
  </article>

</body>
</html>
```